Presentation for partners template design for a healthy bakery

A bakery that makes healthy homemade cupcakes, needs a presentation template for wholesale partners. We need 3-4 template pages with pictures and text blocks, one template that can accomodate a pricing table. Just to give you an idea for the templates our final presentation will include:
1. Cover page with logo
2. Intro page about us
3. Detailed description of products
4. Menu table: cupcakes with wholesale pricing
5. Contact page
Updates

Target Market(s)

Food stores, cafés, fitness clubs, pastry shops, etc.

Industry/Entity Type

Bakery

Font styles to use
Sans Serif

Colors
fee3d4
fce8d3
eaf2ce
cadf82
ffffff
000000
cfeae6
ec1f27
86cfc6

Requirements
Must have
• Presentation needs to look serious and professional. The design needs to give an eco feel: we use recycled materials in our packaging and production. Please make sure the fonts you use support Cyrillic.
Nice to have
• The format of pages is either square or horizontal A4. The company mint colour (see logo attached) needs to be used, but other colours can be used in addition (lime green, peach, black, chocolate brown, red, etc). Craft paper texture (like our packaging, see photos) would be nice to have.

```html
<!DOCTYPE html>
<html lang="en">
<head>
<meta charset="utf-8">
<title>Contact</title>
<link rel="stylesheet" href="https://fonts.googleapis.com/css2?family=Dosis:wght@400;500&display=swap">
<style>
  :root {
    --lime: #cadf82;
    --mint: #86cfc6;
    --text-lime: #e3ee9a;
    --photo-dark: #544a50;
    --photo-mid: #6c6466;
    --photo-mint: #6f908b;
  }
  html, body {
    margin: 0;
    padding: 0;
    overflow: hidden;
    background: #ffffff;
  }
  .page {
    position: relative;
    width: 1200px;
    height: 848px;
    overflow: hidden;
    font-family: "Dosis", sans-serif;
  }
  .page-shapes {
    position: absolute;
    inset: 0;
  }
  .contact-title {
    position: absolute;
    left: 0;
    width: 1240px;
    top: 138px;
    margin: 0;
    text-align: center;
    font-weight: 400;
    font-size: 88px;
    letter-spacing: 2px;
    color: var(--mint);
  }
  .contact-list {
    position: absolute;
    left: 508px;
    top: 374px;
    margin: 0;
    padding: 0;
    list-style: none;
  }
  .contact-item {
    position: relative;
    height: 20px;
    padding-left: 64px;
    font-size: 18px;
    line-height: 20px;
    color: var(--text-lime);
  }
  .contact-item + .contact-item { margin-top: 20px; }
  .contact-item:nth-child(2) { margin-top: 22px; }
  .contact-item::before {
    content: "";
    position: absolute;
    left: 0;
    top: 0;
    width: 21px;
    height: 21px;
    border-radius: 50%;
    background: var(--mint);
  }
  .contact-item.is-web::before { background: var(--lime); }
</style>
</head>
<body>
<main class="page">
  <svg class="page-shapes" width="1200" height="848" viewBox="0 0 1200 848" xmlns="http://www.w3.org/2000/svg">
    <defs>
      <radialGradient id="photoTone" cx="0.5" cy="0.45" r="0.6">
        <stop offset="0" stop-color="var(--photo-mint)"/>
        <stop offset="0.55" stop-color="var(--photo-mid)"/>
        <stop offset="1" stop-color="var(--photo-dark)"/>
      </radialGradient>
    </defs>
    <rect class="hero-photo" role="img" aria-label="Photo of a cupcake with mint frosting, pink hearts and sprinkles on a polka-heart napkin" x="0" y="0" width="1200" height="848" fill="url(#photoTone)"/>
    <path class="side-band" d="M0 0 H132 C126 260 112 560 108 848 H0 Z" fill="var(--lime)"/>
    <path class="bottom-band" d="M104 741 C280 775 520 765 720 738 S1080 708 1200 706 V848 H104 Z" fill="var(--mint)"/>
  </svg>

  <h1 class="contact-title">CONTACT</h1>

  <ul class="contact-list">
    <li class="contact-item">your address</li>
    <li class="contact-item">123-4567890</li>
    <li class="contact-item">hello@mintcrumb.com</li>
    <li class="contact-item is-web">www.mintcrumb.com</li>
  </ul>
</main>
</body>
</html>
```